Business card for Eyelash extension salon in MARLOW VALE,California USA

We need new business card for our salon in MARLOW VALE. The salon name is 'Lashvora' . We would like to have...Business name: Lashvora Name of person: will provide later Address 6812 N.Calder Ridge Ave MARLOW VALE , CA 90210 Phone: will provide later (Text only) Web: www.lashvorastudio-demo.com Instagram icon, Facebook icon follow us for seasonal campaign and news @lashvorastudiodemo Design should look elegant, high-end, clean, simple, cohesive with my brand. Please refer my brand board. Business name color will be metallic bronzy color. Im thinking grey background or white background. Thanks

Target Market(s)

25-35. Gender neutral. People who are in Entertainment business industry.
This is High-end Eyelash extension salon in MARLOW VALE

Industry/Entity Type

Beauty Salon

Contact Information for Business Card

Business name: Lashvora
Name of person: will provide later
Address 6812 N.Calder Ridge Ave MARLOW VALE , CA 90210
Phone: will provide later (Text only)
Web: www.lashvorastudio-demo.com
Instagram icon, Facebook icon
follow us for seasonal campaign and news @lashvorastudiodemo

Requirements
Must have
• Beautiful, elegant, clean and simple look but very attractive and modern
Should not have
• We don't like too clutter, too busy designs.

```html
<!DOCTYPE html>
<html lang="en">
<head>
<meta charset="utf-8">
<title>Lashvora – Business Card</title>
<link href="https://fonts.googleapis.com/css2?family=Caladea:wght@400;700&display=swap" rel="stylesheet">
<style>
  :root {
    --backdrop: #dedede;
    --card-white: #ffffff;
    --bronze: #86654a;
    --stone: #a9a9a9;
    --stone-dark: #9a9a9a;
    --ink: #474747;
    --rule: #b5b5b5;
    --emboss: #c9c9c9;
  }
  * { margin: 0; padding: 0; box-sizing: border-box; }
  html, body {
    width: 1200px; height: 960px; overflow: hidden;
    background: var(--backdrop);
    font-family: "Caladea", Georgia, serif;
  }
  .canvas { position: relative; width: 1200px; height: 960px; }

  .card { position: absolute; width: 600px; height: 343px; overflow: hidden; }
  .card--front { left: 302px; top: 122px; background: var(--card-white); }
  .card--back { left: 300px; top: 495px; background: var(--stone); }

  .social { position: absolute; left: 36px; top: 40px; display: flex; gap: 2px; }
  .social__badge { width: 24px; height: 27px; display: block; }
  .social__badge polygon { fill: var(--stone); }

  .brand { position: absolute; right: 36px; top: 58px; text-align: right; color: var(--bronze); }
  .brand__name { font-size: 54px; font-weight: 400; line-height: 1; letter-spacing: 1px; }
  .brand__place { font-size: 9px; letter-spacing: 1.6px; margin-top: 30px; margin-right: 30px; }

  .person { position: absolute; left: 33px; top: 190px; }
  .person__name { font-size: 26px; font-weight: 700; color: var(--bronze); line-height: 1; letter-spacing: 0.5px; }
  .person__role { font-size: 16px; font-weight: 700; color: var(--stone); line-height: 1; margin-top: 1px; letter-spacing: 0.5px; }

  .divider { position: absolute; left: 34px; right: 36px; top: 241px; height: 1px; background: var(--rule); }

  .contact { position: absolute; top: 253px; font-size: 15px; line-height: 19px; color: var(--ink); }
  .contact--left { left: 34px; }
  .contact--right { right: 34px; text-align: right; }

  .footer-band { position: absolute; left: 0; bottom: 0; width: 600px; height: 34px; }
  .footer-band .band-stone { fill: var(--stone); }
  .footer-band .band-bronze { fill: var(--bronze); }
  .web { position: absolute; right: 26px; bottom: 9px; font-size: 15px; letter-spacing: 1.2px; color: var(--card-white); }

  .back-mark { position: absolute; left: 0; right: 0; top: 100px; text-align: center; color: var(--emboss); }
  .back-mark__name { font-size: 96px; line-height: 1; letter-spacing: 2px; }
  .back-mark__place { font-size: 12px; letter-spacing: 2.4px; margin-top: 40px; color: var(--stone-dark); }
</style>
</head>
<body>
<main class="canvas">

  <section class="card card--front" aria-label="Business card front">
    <div class="social" aria-label="Social media links">
      <svg class="social__badge" viewBox="0 0 24 27" aria-hidden="true"><polygon points="12,0 24,6.75 24,20.25 12,27 0,20.25 0,6.75"/></svg>
      <svg class="social__badge" viewBox="0 0 24 27" aria-hidden="true"><polygon points="12,0 24,6.75 24,20.25 12,27 0,20.25 0,6.75"/></svg>
      <svg class="social__badge" viewBox="0 0 24 27" aria-hidden="true"><polygon points="12,0 24,6.75 24,20.25 12,27 0,20.25 0,6.75"/></svg>
    </div>

    <div class="brand">
      <div class="brand__name">Lashvora</div>
      <div class="brand__place">MARLOW VALE</div>
    </div>

    <div class="person">
      <div class="person__name">MAREN</div>
      <div class="person__role">OWNER</div>
    </div>

    <div class="divider"></div>

    <div class="contact contact--left">
      <div>310.555.0148</div>
      <div>hello@lashvorastudio-demo.com</div>
    </div>
    <div class="contact contact--right">
      <div>6812 N.Calder Ridge Ave</div>
      <div>Marlow Vale, CA 90417</div>
    </div>

    <svg class="footer-band" viewBox="0 0 600 34" aria-hidden="true">
      <polygon class="band-stone" points="0,21 322,21 311,34 0,34"/>
      <polygon class="band-bronze" points="348,0 600,0 600,34 316,34"/>
    </svg>
    <div class="web">www.lashvorastudio-demo.com</div>
  </section>

  <section class="card card--back" aria-label="Business card back">
    <div class="back-mark">
      <div class="back-mark__name">Lashvora</div>
      <div class="back-mark__place">MARLOW VALE</div>
    </div>
  </section>

</main>
</body>
</html>
```